i would like a business card to leave with customers and potential customers for electrical work and for the supply and install of reverse cycle airconditioning in the domestic and commercial market.
I own my own business and im a sole trader. I have an a'class electrical lisence and also a refrigeration lisence so i am
able to offer complete installations in airconditioning by a fully qualified and lisenced tradesman.
im looking for something that comes across as unique and professional.
i had the coluor black and some gold in mind but open to any coluors.
something like Beacon Electrical & Refrigeration
or Beacon Air.
i will use this design on a business card to advertise through summer to help generate installs through the busy season.

Target Market(s)

Mainly domestic house holds through summer who are in need of airconditioning and reliable information to acomadate thier cooling and heating requirements

Industry/Entity Type

Electrical

Requirements
Must have
• Business name- Beacon
My name- Peter Wollaston
My mobile no- 0457 819 302
My email- prwollaston@tarvel.com.au
Installation & Decomissioning of aiconditioning split systems
LIC NO: KTR 407516
Nice to have
• Beacon Electrical & Refrigeration

```html
<!DOCTYPE html>
<html lang="en">
<head>
<meta charset="utf-8">
<title>Beacon Electrical &amp; Refrigeration – Business Card</title>
<link rel="stylesheet" href="https://fonts.googleapis.com/css2?family=Exo+2:wght@400&family=Arimo:wght@400&display=swap">
<style>
  :root {
    --page-bg: #f2f2f2;
    --card-black: #141414;
    --card-charcoal: #2b2b2b;
    --gold: #c98f2c;
    --gold-deep: #9a6a1c;
    --badge-blue: #3e8fd0;
  }
  * { box-sizing: border-box; margin: 0; padding: 0; }
  html, body {
    width: 1200px;
    height: 900px;
    overflow: hidden;
    background: var(--page-bg);
  }
  .canvas {
    position: relative;
    width: 1200px;
    height: 900px;
    display: flex;
    align-items: center;
    justify-content: center;
  }
  .business-card {
    position: relative;
    width: 900px;
    height: 514px;
    background: radial-gradient(ellipse at 45% 40%, var(--card-charcoal) 0%, var(--card-black) 70%);
    color: var(--gold);
    font-family: "Arimo", Arial, sans-serif;
  }
  .brand {
    position: absolute;
    top: 118px;
    left: 52px;
    display: flex;
    align-items: flex-start;
    gap: 22px;
  }
  .brand-mark {
    width: 122px;
    height: 122px;
    background: linear-gradient(135deg, var(--gold) 0%, var(--gold-deep) 100%);
  }
  .brand-name {
    font-family: "Exo 2", "Trebuchet MS", sans-serif;
    font-size: 29px;
    letter-spacing: 1.5px;
    margin-top: 10px;
    color: var(--gold);
  }
  .contact {
    position: absolute;
    right: 58px;
    top: 200px;
    text-align: right;
    line-height: 1.18;
  }
  .contact-name { font-size: 33px; }
  .contact-phone,
  .contact-email { font-size: 25px; }
  .contact-service { font-size: 23px; margin-top: 2px; }
  .licence {
    display: flex;
    justify-content: flex-end;
    align-items: center;
    gap: 14px;
    font-size: 23px;
    margin-top: 8px;
  }
  .licence-badge {
    width: 44px;
    height: 44px;
    background: #ffffff;
    border: 3px solid var(--badge-blue);
  }
</style>
</head>
<body>
  <main class="canvas">
    <section class="business-card">
      <div class="brand">
        <div class="brand-mark"></div>
        <h1 class="brand-name">Beacon Electrical &amp; Refrigeration</h1>
      </div>
      <div class="contact">
        <p class="contact-name">Peter Wollaston</p>
        <p class="contact-phone">0457 819 302</p>
        <p class="contact-email">prwollaston@tarvel.com.au</p>
        <p class="contact-service">Installation &amp; Decomissioning of aiconditioning split systems</p>
        <div class="licence">
          <span>LIC NO: KTR 407516</span>
          <span class="licence-badge" role="img" aria-label="Licensing certification badge"></span>
        </div>
      </div>
    </section>
  </main>
</body>
</html>
```